Adaptive GS Conversion & Enhancement B2B Site

We are looking to convert our current page to the adaptove Grid System (http://brisk.417.io/) and if there are some general enhancements, we would not complain :-)

We would expect delivery of static html for the following pages:
- home - http://www.velmira.com/
- detail - e.g. http://www.velmira.com/products/products.html
- help - http://www.velmira.com/help/te_reports/customer_approval.html

Our objective is to convert the page to a different system which is then based on the Adapt.js - from mobile.css to 2520.css

Target Market(s)

Business looking for Professional Services Project Management

Requirements
Must have
• Use of http://brisk.417.io/
Should not have
• Flash, or other frameworks (well jQuery is OK if it must be)

```html
<!DOCTYPE html>
<html lang="en">
<head>
<meta charset="utf-8">
<title>Velmira – Time and Expense Management</title>
<link rel="stylesheet" href="https://fonts.googleapis.com/css2?family=Open+Sans:wght@400;600;700&family=PT+Sans+Narrow:wght@700&family=Signika:wght@400;600&display=swap">
<style>
:root{
  --orange:#f5a20f;
  --orange-deep:#f26b10;
  --blue:#1a9ad6;
  --blue-dark:#1c5687;
  --sky-top:#5bb6e6;
  --sky-bottom:#1d9be0;
  --text:#444;
  --muted:#666;
  --date:#8a8a8a;
  --footer:#f2f2f2;
  --bar:#3a3a3a;
  --line:#e2e2e2;
}
*{box-sizing:border-box;margin:0;padding:0}
html,body{width:804px;height:1200px;overflow:hidden}
body{position:relative;background:#fff;font-family:"Open Sans",sans-serif;color:var(--text)}
.abs{position:absolute}
a{color:inherit;text-decoration:none}

/* header */
.header{left:0;top:0;width:804px;height:96px;background:linear-gradient(#f3f3f3,#fff 20%)}
.search-tab{left:552px;top:0;width:192px;height:34px}
.search-box{left:568px;top:7px;width:157px;height:19px;background:#fff;border-radius:10px;font-size:8px;color:#999;padding:4px 10px}
.search-box svg{position:absolute;right:8px;top:4px}
.brand{left:34px;top:38px;display:flex;align-items:center;gap:7px;font-weight:600;font-size:24px;color:#222}
.brand-dot{width:24px;height:24px;border-radius:50%;background:var(--blue)}
.nav{left:273px;top:58px;width:507px;height:38px;background:var(--orange);border-radius:3px 3px 0 0;display:flex;align-items:center;justify-content:space-around;font-family:"Signika",sans-serif;font-size:12px;color:#fff;padding:0 6px}
.nav .sep{width:1px;height:14px;background:rgba(255,255,255,.6)}

/* hero */
.hero{left:0;top:96px;width:804px;height:316px;background:linear-gradient(var(--sky-top),var(--sky-bottom))}
.hero-title{left:37px;top:148px;font-family:"PT Sans Narrow",sans-serif;font-weight:700;font-size:25px;color:var(--blue-dark);white-space:nowrap}
.hero-sub{left:37px;top:180px;font-family:"PT Sans Narrow",sans-serif;font-size:18px;color:var(--blue-dark);font-weight:700;white-space:nowrap}
.hero-copy{left:37px;top:211px;width:300px;font-size:10px;line-height:16px;color:#fff}
.hero-copy p+p{margin-top:4px}
.btn-learn{left:36px;top:308px;width:88px;height:28px;border-radius:14px;background:var(--orange);border:1px solid #fff3;color:#fff;font-size:9.5px;font-weight:600;display:flex;align-items:center;justify-content:center}
.hero-art{left:360px;top:130px;width:424px;height:222px;border-radius:10px;background:linear-gradient(#eef3f7,#c9d3da)}
.dots{left:381px;top:374px;display:flex;gap:5px}
.dots i{width:8px;height:8px;border-radius:50%;background:#fff}

/* features panel */
.panel{left:17px;top:389px;width:770px;height:234px;background:linear-gradient(#fff 70%,#f6f6f6);border-radius:5px;box-shadow:0 2px 4px rgba(0,0,0,.15);border-top:4px solid #5fb7e6}
.feature{top:412px;width:224px}
.feature h2{font-family:"Signika",sans-serif;font-weight:400;font-size:15px;color:var(--orange-deep)}
.feature .photo{margin-top:8px;height:81px;border-radius:4px}
.feature p{margin-top:6px;font-size:8.6px;line-height:16px;color:var(--text);padding-left:1px}
.feature .more{display:block;margin-top:4px;font-size:8.6px;font-weight:600;color:var(--orange-deep)}

/* growth column */
.growth-title{left:28px;top:650px;font-weight:400;font-size:15.5px;color:#333;line-height:20px;white-space:nowrap}
.growth-title strong{display:block;font-family:"Signika",sans-serif;font-weight:400;color:var(--blue);font-size:16.5px}
.growth-copy{left:28px;width:250px;font-size:8.8px;line-height:16px;color:var(--muted);white-space:nowrap}
.checklist{left:28px;top:811px;list-style:none;font-size:9.3px;color:#222}
.checklist li{height:21.4px;line-height:16px;padding-left:16px;position:relative;white-space:nowrap}
.checklist li::before{content:"";position:absolute;left:6px;top:5px;border:3px solid transparent;border-left:4px solid #333}
.pill{height:19px;border-radius:10px;background:var(--blue);color:#fff;font-size:8px;font-weight:600;display:flex;align-items:center;justify-content:center}
.divider{top:652px;width:1px;height:285px;background:var(--line)}
.col-title{font-family:"Signika",sans-serif;font-weight:400;font-size:15px;color:var(--blue)}
.project{left:296px;width:230px;display:flex;gap:8px}
.project .thumb{width:60px;height:54px;border-radius:3px;flex:none}
.project h4{font-size:8.6px;font-weight:600;color:#222}
.project p{font-size:8.6px;line-height:16px;color:#444}
.news{left:556px;width:225px;display:flex;gap:10px}
.news .date{width:40px;text-align:center;font-family:"Signika",sans-serif;font-size:19px;line-height:24px;color:var(--date)}
.news p{font-size:9.3px;line-height:16px;color:var(--muted)}
.news .more{display:block;margin-top:4px;font-size:9.3px;font-weight:600;color:#555}

/* footer */
.footer{left:0;top:982px;width:804px;height:184px;background:var(--footer)}
.fcol{top:1008px}
.fcol h5{font-size:11px;font-weight:600;color:#333;margin-bottom:8px}
.fcol li{list-style:none;font-size:9.3px;line-height:20px;color:var(--muted)}
.fdiv{top:1010px;width:1px;height:115px;background:#dcdcdc}
.social{display:flex;gap:9px;margin-top:8px}
.social i{width:20px;height:20px;border-radius:3px;background:#555}
.social-links{margin-top:10px;font-size:8.6px;color:#444;white-space:nowrap}
.badge-a{left:632px;top:1010px;width:117px;height:44px;border-radius:5px;background:#1a5d8f}
.badge-b{left:634px;top:1062px;width:158px;height:48px;background:#fff;border-bottom:10px solid #e41b17}
.bottom{left:0;top:1166px;width:804px;height:34px;background:var(--bar);font-size:8.3px;color:#ddd;padding:13px 34px}
</style>
</head>
<body>

<header>
  <div class="abs header"></div>
  <svg class="abs search-tab" viewBox="0 0 192 34" aria-hidden="true"><polygon points="0,0 192,0 178,34 12,34" fill="#e6e6e6"/></svg>
  <div class="abs search-box">Search here..
    <svg width="10" height="10" viewBox="0 0 10 10"><circle cx="4" cy="4" r="3" fill="none" stroke="#888" stroke-width="1.4"/><line x1="6.3" y1="6.3" x2="9" y2="9" stroke="#888" stroke-width="1.6"/></svg>
  </div>
  <a class="abs brand" href="http://www.velmira.com/"><span class="brand-dot"></span>Velmira</a>
  <nav class="abs nav">
    <a href="#">Home</a><span class="sep"></span>
    <a href="#">Products</a><span class="sep"></span>
    <a href="#">Services</a><span class="sep"></span>
    <a href="#">Support</a><span class="sep"></span>
    <a href="#">Blog</a><span class="sep"></span>
    <a href="#">About Us</a><span class="sep"></span>
    <a href="#">Contact Us</a>
  </nav>
</header>

<section>
  <div class="abs hero"></div>
  <h1 class="abs hero-title">Easy Capture Time and Expenses</h1>
  <div class="abs hero-sub">Automate management and reporting</div>
  <div class="abs hero-copy">
    <p>Cras id elit. Integer quis urna. Ut ante enim, dapibus malesuada, fringilla eu, condimentum quis, tellus.</p>
    <p>Mauris vel lacus vitae felis vestibulum volutpat. Etiam est nunc, venenatis in, tristique eu, imperdiet ac, nisl. Cum sociis natoque penatibus et magnis dis parturient montes</p>
  </div>
  <a class="abs btn-learn" href="#">Learn More</a>
  <div class="abs hero-art" role="img" aria-label="Three laptops showing the cloud service dashboard"></div>
  <div class="abs dots"><i></i><i></i><i></i><i></i></div>
</section>

<section>
  <div class="abs panel"></div>
  <article class="abs feature" style="left:45px">
    <h2>Why Choose Us</h2>
    <div class="photo" role="img" aria-label="Photo of two businessmen greeting each other" style="background:linear-gradient(90deg,#c9cdd0,#e6e6e4 50%,#a9b0b5)"></div>
    <p>Praesent vestibulum aenean nonummy hendrerit mauris. Hasellus porta. Fusce suscipit varius mi cum sociis natoque</p>
    <a class="more" href="#">Read More</a>
  </article>
  <article class="abs feature" style="left:295px">
    <h2>Services We Provide</h2>
    <div class="photo" role="img" aria-label="Photo of a man touching a cloud network diagram in the sky" style="background:linear-gradient(90deg,#8a7d70,#2f7fd4 45%,#1c6bd0)"></div>
    <p>Praesent vestibulum aenean nonummy hendrerit mauris. Hasellus porta. Fusce suscipit varius mi cum sociis natoque</p>
    <a class="more" href="#">Read More</a>
  </article>
  <article class="abs feature" style="left:546px">
    <h2>Professional &amp; Experts</h2>
    <div class="photo" role="img" aria-label="Photo of a smiling business team" style="background:linear-gradient(90deg,#3b3c44,#cfcfd2 50%,#2e2f36)"></div>
    <p>Praesent vestibulum aenean nonummy hendrerit mauris. Hasellus porta. Fusce suscipit varius mi cum sociis natoque</p>
    <a class="more" href="#">Read More</a>
  </article>
</section>

<section>
  <h2 class="abs growth-title">Let's create your company's<strong>GROWTH STRATEGY</strong></h2>
  <p class="abs growth-copy" style="top:698px">Velmira's line of value-added services speeds product<br>deployment, maximizes return on investment and<br>enhances overall customer satisfaction.</p>
  <p class="abs growth-copy" style="top:750px">&nbsp;Cras id elit. Integer quis urna.</p>
  <p class="abs growth-copy" style="top:769px">Ut ante enim, dapibus malesuada, fringilla eu, condi-<br>mentum quis, tellus.</p>
  <ul class="abs checklist">
    <li>Praesent vestibulum aenean nonummy</li>
    <li>Fusce suscipit varius mi cum sociis</li>
    <li>Natoque penatibus et magnis dis</li>
    <li>Parturient montes nascetur ridiculus</li>
    <li>Fusce feugiat malesuada odio</li>
  </ul>
  <a class="abs pill" href="#" style="left:28px;top:925px;width:57px">Read More</a>
  <div class="abs divider" style="left:274px"></div>

  <h2 class="abs col-title" style="left:293px;top:656px">Recent Projects</h2>
  <div class="abs project" style="top:687px">
    <div class="thumb" role="img" aria-label="Photo of a project team" style="background:linear-gradient(135deg,#c98b6e,#e9e3dc)"></div>
    <div><h4>Project Tittle</h4><p>Aenean nonummy hendrerit mauris. Hasellus porta. Fusce suscipit varius mi cum sociis natoque</p></div>
  </div>
  <div class="abs project" style="top:764px">
    <div class="thumb" role="img" aria-label="Photo of two business colleagues" style="background:linear-gradient(135deg,#2c3340,#e7e8ea)"></div>
    <div><h4>Project Tittle</h4><p>Aenean nonummy hendrerit mauris. Hasellus porta. Fusce suscipit varius mi cum sociis natoque</p></div>
  </div>
  <div class="abs project" style="top:842px">
    <div class="thumb" role="img" aria-label="Photo of a growth chart with notes" style="background:linear-gradient(135deg,#f1ecdc,#d8c88a)"></div>
    <div><h4>Project Tittle</h4><p>Aenean nonummy hendrerit mauris. Hasellus porta. Fusce suscipit varius mi cum sociis natoque</p></div>
  </div>
  <a class="abs pill" href="#" style="left:305px;top:923px;width:57px">Read More</a>
  <div class="abs divider" style="left:536px"></div>

  <h2 class="abs col-title" style="left:554px;top:656px">Latest News</h2>
  <div class="abs news" style="top:688px">
    <div class="date">20<br>NOV</div>
    <div><p>Praesent vestibulum aenean nonummy hendrerit mauris. Hasellus porta. Fusce suscipit varius mi</p><a class="more" href="#">Learn More</a></div>
  </div>
  <div class="abs news" style="top:766px">
    <div class="date">10<br>NOV</div>
    <div><p>Praesent vestibulum aenean nonummy hendrerit mauris. Hasellus porta. Fusce suscipit varius mi</p><a class="more" href="#">Learn More</a></div>
  </div>
  <div class="abs news" style="top:841px">
    <div class="date">10<br>NOV</div>
    <div><p>Praesent vestibulum aenean nonummy hendrerit mauris. Hasellus porta. Fusce suscipit varius mi</p><a class="more" href="#">Learn More</a></div>
  </div>
  <a class="abs pill" href="#" style="left:559px;top:922px;width:58px">Read More</a>
</section>

<footer>
  <div class="abs footer"></div>
  <div class="abs fcol" style="left:33px"><h5>Company</h5><ul><li>About Company</li><li>What We Do</li><li>Why We Are</li><li>Recent Blog</li><li>Services Offerd</li></ul></div>
  <div class="abs fdiv" style="left:128px"></div>
  <div class="abs fcol" style="left:158px"><h5>Support</h5><ul><li>Help</li><li>FAQ</li><li>Term of Use</li><li>Support</li><li>Contact Us</li></ul></div>
  <div class="abs fdiv" style="left:238px"></div>
  <div class="abs fcol" style="left:270px"><h5>Contact Information</h5><ul><li>Phone:+1 (555) 014-2290</li><li>418 Harbor Crest Lane,</li><li>Suite 210-045</li><li>Millbrook, CA 90210</li></ul></div>
  <div class="abs fdiv" style="left:406px"></div>
  <div class="abs fcol" style="left:440px"><h5>Get In Touch</h5>
    <div class="social"><i></i><i></i><i></i><i></i></div>
    <div class="social-links">Circlebook&nbsp; /&nbsp; Chirpline&nbsp; /&nbsp; Streamtube&nbsp; /&nbsp; RSS</div>
  </div>
  <div class="abs fdiv" style="left:606px"></div>
  <div class="abs badge-a" role="img" aria-label="Accreditation badge"></div>
  <div class="abs badge-b" role="img" aria-label="Partner badge"></div>
  <div class="abs bottom">© 2012 Company Name.&nbsp; All right resreved</div>
</footer>

</body>
</html>
```